Meridel Haulage - Website

A clean, not cluttered informative website for our business. We specialize in the transportation of radioactive materials across North America. The site is mostly for information about our company and will not be used to attract business but will be used to attract employee's mainly drivers. Driver's are very hard to find in our area. One of the pages needs to be a job's posting page with an apply now button. Either an application can be filled out there or a resume can be uploaded which ever functionality works better. I would like a website that I can easily edit, ability to change text and photos.

Number of Pages Required

5+ page

Colors

Designer to choose colors to be used in the design.

Requirements
Must have
• Home - About - Services - Jobs - Contact pages
• A way prospective employee's can apply or upload their resume to be emailed to me
• Very clean apperance
Should not have
• I don't want it to be busy

```html
<!DOCTYPE html>
<html lang="en">
<head>
<meta charset="utf-8">
<title>Meridel Haulage</title>
<link href="https://fonts.googleapis.com/css2?family=Jost:wght@400;500;600&family=Orbitron:wght@700;800&display=swap" rel="stylesheet">
<style>
:root{
  --blue:#2f5cb5;
  --blue-deep:#24498f;
  --ink:#333;
  --text:#4a4a4a;
  --muted:#777;
  --line:#e6e6e6;
  --footer:#343434;
  --white:#fff;
}
*{margin:0;padding:0;box-sizing:border-box}
html,body{width:1200px;height:3309px;overflow:hidden}
body{font-family:"Jost",sans-serif;color:var(--text);background:var(--white);position:relative}
section,header,footer,div{position:relative}
.abs{position:absolute}
.display{font-family:"Orbitron",sans-serif;font-weight:800;letter-spacing:2px;text-transform:uppercase}

/* top bar */
.topbar{height:44px;background:var(--blue);color:var(--white);font-size:13px}
.topbar .info{position:absolute;left:141px;top:0;height:44px;display:flex;align-items:center;gap:26px}
.topbar .info span{display:flex;align-items:center;gap:7px}
.topbar .social{position:absolute;right:145px;top:15px;display:flex;gap:18px}
.topbar .social i{display:block;width:13px;height:13px;border-radius:50%;background:rgba(255,255,255,.85)}

/* nav */
.nav{height:84px;background:var(--white)}
.brand{position:absolute;left:141px;top:22px;font-size:30px;font-weight:600;color:var(--blue);line-height:40px;letter-spacing:.5px}
.menu{position:absolute;top:34px;left:0;width:1200px;height:20px;list-style:none;font-size:13px;text-transform:uppercase;color:var(--ink)}
.menu li{position:absolute}
.menu li.active{color:var(--blue);border-bottom:1px solid var(--blue)}

/* hero */
.hero{height:565px;background:linear-gradient(180deg,#8d8170 0%,#5f554a 45%,#3f372f 100%);color:var(--white);text-align:center}
.hero .kicker{position:absolute;top:181px;width:100%;font-size:19px;letter-spacing:5px;font-family:"Orbitron",sans-serif;font-weight:700}
.hero h1{position:absolute;top:215px;width:100%;font-size:38px;line-height:52px;letter-spacing:5px}
.hero .btn-outline{position:absolute;left:512px;top:353px;width:176px;height:48px;border:2px solid var(--white);border-radius:24px;font-size:20px;line-height:44px}
.hero .arrow{position:absolute;top:264px;width:34px;height:34px;border:1.5px solid rgba(255,255,255,.8);border-radius:50%}

/* about */
.about{height:509px}
.about h2{position:absolute;left:141px;top:70px;font-size:24px;color:var(--ink)}
.about p{position:absolute;left:141px;width:446px;font-size:11.5px;line-height:18px;text-align:justify;color:var(--text)}
.btn{position:absolute;background:var(--blue);color:var(--white);border-radius:20px;font-size:14px;text-align:center;display:flex;align-items:center;justify-content:center;gap:8px}
.about .truck{position:absolute;left:620px;top:90px;width:570px;height:440px;border-radius:40px 10px 10px 40px;background:linear-gradient(90deg,#f0a020 0%,#e89116 30%,#cfd3d8 45%,#9aa2ab 75%,#d7dbe0 100%);opacity:.92;z-index:2}

/* services */
.services{height:497px;background:linear-gradient(180deg,#3462b9 0%,#2f5cb5 60%,#3a66bb 100%);overflow:hidden}
.services h2{position:absolute;top:76px;width:100%;text-align:center;color:var(--white);font-size:25px}
.services .label{position:absolute;color:var(--white);font-size:18px;white-space:nowrap}
.services .label.r{text-align:right}
.services .truck{position:absolute;left:495px;top:340px;width:210px;height:115px;border-radius:8px;background:linear-gradient(90deg,#f0a020 0%,#f0a020 40%,#c8ccd2 55%,#9ea6af 100%)}

/* blog */
.blog{height:595px}
.blog h2{position:absolute;top:75px;width:100%;text-align:center;font-size:25px;color:var(--ink)}
.card{position:absolute;top:154px;width:219px;height:315px;background:var(--white);border-radius:6px;box-shadow:0 2px 8px rgba(0,0,0,.14);overflow:hidden}
.card .photo{height:155px}
.card .photo.dusk{background:linear-gradient(180deg,#e0a050 0%,#b0542a 55%,#4a2b20 100%)}
.card .photo.day{background:linear-gradient(180deg,#6f8fb8 0%,#9cb3cf 50%,#4a5a6e 100%)}
.card .date{position:absolute;left:9px;top:0;width:34px;height:40px;background:var(--blue);color:var(--white);font-size:17px;line-height:18px;padding:4px 0 0 6px}
.card .date small{display:block;font-size:9px;line-height:10px}
.card h3{margin:22px 12px 6px;font-size:14px;font-weight:600;color:var(--ink)}
.card p{margin:0 12px;font-size:9.5px;line-height:14px;color:var(--muted)}
.card .meta{position:absolute;left:12px;right:12px;bottom:12px;display:flex;justify-content:space-between;font-size:10px;color:var(--muted);align-items:center;padding-top:8px;border-top:1px solid var(--line)}
.card .meta span{display:flex;align-items:center;gap:4px}

/* careers */
.careers{height:430px;background:linear-gradient(90deg,#2d59ad 0%,#2f5cb5 55%,#4e77c2 100%);color:var(--white)}
.careers .person{position:absolute;left:99px;top:22px;width:265px;height:408px;border-radius:120px 120px 0 0;background:linear-gradient(180deg,#e0b79c 0%,#c44b2c 35%,#6f87a8 70%,#5b6f8d 100%)}
.careers h2{position:absolute;left:401px;top:80px;font-size:25px}
.careers p{position:absolute;left:401px;top:133px;width:640px;font-size:12.5px;line-height:19px}
.careers ul{position:absolute;left:401px;top:206px;list-style:none;font-size:12.5px}
.careers li{height:33px}
.careers .btn-light{position:absolute;left:399px;top:316px;width:126px;height:33px;background:var(--white);color:var(--blue);border-radius:17px;font-size:14px;display:flex;align-items:center;justify-content:center;gap:8px}

/* newsletter */
.newsletter{height:272px}
.newsletter .plane{position:absolute;left:250px;top:100px;width:210px;height:150px;background:linear-gradient(135deg,#f4f4f4,#ececec);clip-path:polygon(0 70%,100% 0,60% 100%);}
.newsletter h2{position:absolute;right:792px;top:90px;text-align:right;font-size:25px;line-height:36px;color:var(--blue)}
.newsletter .divider{position:absolute;left:432px;top:33px;width:1px;height:177px;background:#ddd}
.newsletter .lead{position:absolute;left:470px;top:84px;font-size:13px;color:var(--ink)}
.newsletter .field{position:absolute;left:470px;top:118px;width:457px;height:39px;border-radius:20px;box-shadow:0 1px 6px rgba(0,0,0,.18);background:var(--white);font-size:11px;color:var(--ink);padding:12px 0 0 20px}
.newsletter .field .submit{position:absolute;right:0;top:0;width:142px;height:39px;border-radius:20px;background:var(--blue);color:var(--white);font-size:14px;text-align:center;line-height:39px}

/* footer */
.footer{height:269px;background:var(--footer);color:#ddd}
.footer h4{position:absolute;top:55px;font-size:16px;font-weight:400;color:var(--white);padding-bottom:6px;border-bottom:1px dashed #888}
.footer .links{position:absolute;left:143px;top:82px;list-style:none;font-size:12px;line-height:24.5px}
.footer .links li.active{color:#4f7fd6}
.footer .contact{position:absolute;left:355px;top:86px;list-style:none;font-size:12px}
.footer .contact li{display:flex;gap:12px;align-items:flex-start;margin-bottom:18px;line-height:15px}
.footer .map{position:absolute;left:578px;top:51px;width:256px;height:185px;background:linear-gradient(135deg,#e8e8e8,#d2d2d2);border:3px solid #eee}
.footer .brand-foot{position:absolute;left:878px;top:100px;font-size:26px;font-weight:600;color:var(--white)}
.footer .social{position:absolute;left:882px;top:162px;display:flex;gap:6px}
.footer .social i{display:block;width:23px;height:23px;border-radius:50%;border:1.5px solid #ccc}
.footer .social i.on{background:var(--blue);border-color:var(--blue)}
.copybar{height:44px;background:var(--blue);color:var(--white);font-size:11px}
.copybar span{position:absolute;top:15px}
</style>
</head>
<body>

<div class="topbar">
  <div class="info">
    <span><svg width="10" height="13" viewBox="0 0 10 13"><path d="M5 0a5 5 0 0 0-5 5c0 4 5 8 5 8s5-4 5-8a5 5 0 0 0-5-5zm0 7a2 2 0 1 1 0-4 2 2 0 0 1 0 4z" fill="#fff"/></svg>North America</span>
    <span><svg width="12" height="12" viewBox="0 0 12 12"><path d="M2.5 0 4.5 3 3.3 4.5c.8 1.7 2.2 3.1 3.9 3.9L8.7 7.2 12 9.2 10.8 12C5 11.6.4 7 0 1.2z" fill="#fff"/></svg>123-456-7890</span>
    <span><svg width="13" height="10" viewBox="0 0 13 10"><rect x=".5" y=".5" width="12" height="9" fill="none" stroke="#fff"/><path d="M.5.5 6.5 5.5 12.5.5" fill="none" stroke="#fff"/></svg>info@meridelhaulage.com</span>
  </div>
  <div class="social"><i></i><i></i><i></i><i></i><i></i></div>
</div>

<header class="nav">
  <div class="brand">Meridel Haulage</div>
  <ul class="menu">
    <li class="active" style="left:540px">Home</li>
    <li style="left:632px">About</li>
    <li style="left:722px">Services</li>
    <li style="left:827px">Jobs</li>
    <li style="left:908px">Blog</li>
    <li style="left:995px">Contact</li>
  </ul>
</header>

<section class="hero" role="img" aria-label="Tanker truck driving on a dusty road at sunset">
  <div class="kicker">WE SPECIALIZE IN</div>
  <h1 class="display">The Transportation of<br>Radioactive Materials</h1>
  <div class="btn-outline">Contact</div>
  <div class="arrow" style="left:71px"><svg width="31" height="31" viewBox="0 0 31 31"><path d="M18 10l-5 5.5 5 5.5" fill="none" stroke="#fff" stroke-width="1.6"/></svg></div>
  <div class="arrow" style="left:1095px"><svg width="31" height="31" viewBox="0 0 31 31"><path d="M13 10l5 5.5-5 5.5" fill="none" stroke="#fff" stroke-width="1.6"/></svg></div>
</section>

<section class="about">
  <h2 class="display">About</h2>
  <p style="top:148px">Lorem ipsum dolor sit amet, consectetuer adipiscing elit, sed diam nonummy nibh euismod tincidunt ut laoreet dolore magna aliquam erat volutpat. Ut wisi enim ad minim veniam, quis nostrud exerci tation ullamcorper suscipit lobortis nisl ut aliquip ex ea commodo consequat. Duis autem vel eum iriure dolor in hendrerit in vulputate velit esse molestie consequat, praesent luptatum zzril delenit augue duis dolore te feugait nulla facilisi.</p>
  <p style="top:292px">Lorem ipsum dolor sit amet, consectetuer adipiscing elit, sed diam nonummy nibh euismod tincidunt ut laoreet dolore magna aliquam erat volutpat. Ut wisi enim ad minim veniam, quis nostrud exerci tation ullamcorper suscipit lobortis nisl ut aliquip ex ea commodo consequat.</p>
  <div class="btn" style="left:141px;top:403px;width:141px;height:34px">Read More <svg width="16" height="8" viewBox="0 0 16 8"><path d="M0 4h14M11 1l3 3-3 3" fill="none" stroke="#fff" stroke-width="1.5"/></svg></div>
  <div class="truck" role="img" aria-label="Orange tanker truck with a polished steel tank"></div>
</section>

<section class="services">
  <h2 class="display">Services</h2>
  <svg class="abs" style="left:0;top:0" width="1200" height="497" viewBox="0 0 1200 497">
    <circle cx="600" cy="497" r="258" fill="#e6e6e6"/>
    <circle cx="600" cy="497" r="218" fill="#fff"/>
    <g fill="#555">
      <circle cx="547" cy="316" r="3.5"/><circle cx="653" cy="316" r="3.5"/>
      <circle cx="474" cy="371" r="3.5"/><circle cx="726" cy="371" r="3.5"/>
      <circle cx="424" cy="435" r="3.5"/><circle cx="776" cy="435" r="3.5"/>
    </g>
    <g fill="#555" stroke="#fff" stroke-width="3">
      <circle cx="527" cy="248" r="36"/><circle cx="673" cy="248" r="36"/>
      <circle cx="428" cy="305" r="36"/><circle cx="772" cy="305" r="36"/>
      <circle cx="362" cy="406" r="36"/><circle cx="834" cy="406" r="36"/>
    </g>
    <!-- staff -->
    <g fill="#fff"><circle cx="527" cy="240" r="6"/><circle cx="514" cy="244" r="4.5"/><circle cx="540" cy="244" r="4.5"/><path d="M516 262a11 11 0 0 1 22 0z"/><path d="M505 260a9 9 0 0 1 12-7v7z"/><path d="M549 260a9 9 0 0 0-12-7v7z"/></g>
    <!-- prices -->
    <g fill="none" stroke="#fff" stroke-width="2"><rect x="660" y="232" width="20" height="28" rx="2"/><path d="M664 240h12M664 246h4M672 246h4M664 252h4M672 252h4"/><circle cx="684" cy="256" r="6" fill="#555"/></g>
    <!-- 24/7 gear -->
    <g fill="none" stroke="#fff" stroke-width="3.5" stroke-dasharray="4 3"><circle cx="428" cy="305" r="12"/></g>
    <circle cx="428" cy="305" r="5" fill="#fff"/>
    <!-- experience briefcase -->
    <g fill="#fff"><rect x="757" y="296" width="30" height="21" rx="2"/><rect x="766" y="290" width="12" height="6" rx="1" fill="none" stroke="#fff" stroke-width="2"/></g>
    <rect x="757" y="303" width="30" height="2" fill="#555"/>
    <!-- certified -->
    <g fill="#fff"><circle cx="360" cy="398" r="7"/><path d="M346 420a14 14 0 0 1 28 0z"/><circle cx="373" cy="414" r="5" stroke="#555" stroke-width="2"/></g>
    <!-- clients -->
    <g fill="#fff"><circle cx="834" cy="397" r="7"/><path d="M820 422a14 14 0 0 1 28 0z"/></g>
  </svg>
  <div class="truck" role="img" aria-label="Orange tanker truck, front three-quarter view"></div>
  <div class="label r" style="right:726px;top:195px">We Have Trained Staff</div>
  <div class="label" style="left:730px;top:195px">Our Prices Are Affordable</div>
  <div class="label r" style="right:834px;top:290px">24/7 Services</div>
  <div class="label" style="left:838px;top:290px">Year Of Experience</div>
  <div class="label r" style="right:904px;top:394px">Certified Experts</div>
  <div class="label" style="left:902px;top:394px">Satisfied Clients</div>
</section>

<section class="blog">
  <h2 class="display">Latest Blog</h2>
  <article class="card" style="left:141px">
    <div class="photo day" role="img" aria-label="Tanker truck on a highway at dusk"></div>
    <div class="date">28<small>Jan</small></div>
    <h3>Lorem ipsum dolor sit amet</h3>
    <p>It is a long established fact that a reader will be distracted by the readable content of a page when looking at its layout.</p>
    <div class="meta"><span>&#9670; Article</span><span>&#9632; 23 &nbsp;&#9673; 684</span></div>
  </article>
  <article class="card" style="left:373px">
    <div class="photo dusk" role="img" aria-label="Tanker truck at sunset"></div>
    <div class="date">28<small>Jan</small></div>
    <h3>Lorem ipsum dolor sit amet</h3>
    <p>It is a long established fact that a reader will be distracted by the readable content of a page when looking at its layout.</p>
    <div class="meta"><span>&#9670; Article</span><span>&#9632; 23 &nbsp;&#9673; 684</span></div>
  </article>
  <article class="card" style="left:607px">
    <div class="photo day" role="img" aria-label="Tanker truck on a highway at dusk"></div>
    <div class="date">28<small>Jan</small></div>
    <h3>Lorem ipsum dolor sit amet</h3>
    <p>It is a long established fact that a reader will be distracted by the readable content of a page when looking at its layout.</p>
    <div class="meta"><span>&#9670; Article</span><span>&#9632; 23 &nbsp;&#9673; 684</span></div>
  </article>
  <article class="card" style="left:838px">
    <div class="photo dusk" role="img" aria-label="Tanker truck at sunset"></div>
    <div class="date">28<small>Jan</small></div>
    <h3>Lorem ipsum dolor sit amet</h3>
    <p>It is a long established fact that a reader will be distracted by the readable content of a page when looking at its layout.</p>
    <div class="meta"><span>&#9670; Article</span><span>&#9632; 23 &nbsp;&#9673; 684</span></div>
  </article>
  <div class="btn" style="left:512px;top:494px;width:176px;height:34px">View all Blog Post <svg width="16" height="8" viewBox="0 0 16 8"><path d="M0 4h14M11 1l3 3-3 3" fill="none" stroke="#fff" stroke-width="1.5"/></svg></div>
</section>

<section class="careers">
  <div class="person" role="img" aria-label="Smiling truck driver in a red vest giving a thumbs up"></div>
  <h2 class="display">Career Opportunities</h2>
  <p>It is a long established fact that a reader will be distracted by the readable content of a page when looking at its layout. The point of using Lorem Ipsum is that it has a more-or-less normal distribution of letters, as opposed to using 'Content here, content here', making it look like readable English.</p>
  <ul><li>&gt;&gt; Lorem ipsum dolor sit amet</li><li>&gt;&gt; Lorem ipsum dolor sit amet</li><li>&gt;&gt; Lorem ipsum dolor sit amet</li></ul>
  <div class="btn-light">Apply Now <svg width="16" height="8" viewBox="0 0 16 8"><path d="M0 4h14M11 1l3 3-3 3" fill="none" stroke="#2f5cb5" stroke-width="1.5"/></svg></div>
</section>

<section class="newsletter">
  <div class="plane" role="img" aria-label="Faint paper plane"></div>
  <h2 class="display">Newsletter<br>Sign Up</h2>
  <div class="divider"></div>
  <div class="lead">Subscribe to our newsletter to get the latest scoop right to your inbox</div>
  <div class="field">Enter your email address<div class="submit">Subscribe</div></div>
</section>

<footer class="footer">
  <h4 style="left:143px">Quick Links</h4>
  <ul class="links"><li class="active">&gt;&gt; Home</li><li>&gt;&gt; About</li><li>&gt;&gt; Services</li><li>&gt;&gt; Job</li><li>&gt;&gt; Blog</li><li>&gt;&gt; Contact</li></ul>
  <h4 style="left:355px">Contact Us</h4>
  <ul class="contact">
    <li><svg width="12" height="12" viewBox="0 0 12 12"><path d="M2.5 0 4.5 3 3.3 4.5c.8 1.7 2.2 3.1 3.9 3.9L8.7 7.2 12 9.2 10.8 12C5 11.6.4 7 0 1.2z" fill="#ddd"/></svg>123-456-7890</li>
    <li><svg width="13" height="10" viewBox="0 0 13 10"><rect width="13" height="10" fill="#ddd"/><path d="M0 0 6.5 5.5 13 0" fill="none" stroke="#343434"/></svg>info@meridelhaulage.com</li>
    <li><svg width="13" height="12" viewBox="0 0 13 12"><rect y="1" width="13" height="10" rx="1" fill="#ddd"/></svg>1234567890</li>
    <li><svg width="10" height="13" viewBox="0 0 10 13"><path d="M5 0a5 5 0 0 0-5 5c0 4 5 8 5 8s5-4 5-8a5 5 0 0 0-5-5zm0 7a2 2 0 1 1 0-4 2 2 0 0 1 0 4z" fill="#ddd"/></svg><span>123,Lorem ipsum dolor,<br>North America</span></li>
  </ul>
  <div class="map" role="img" aria-label="Street map showing the office location"></div>
  <div class="brand-foot">Meridel Haulage</div>
  <div class="social"><i class="on"></i><i></i><i></i><i></i><i></i></div>
</footer>

<div class="copybar">
  <span style="left:143px">Copyright © 2019 Meridel Haulage. All Rights Reserved</span>
  <span style="right:145px">Privacy policy/Terms of use</span>
</div>

</body>
</html>
```